Bref créative
Stationary - Morvane Advisory
Business Card, Letterhead & Pen Design
Professional
Helmut Draven
Director
Address line 1
Address line 2
Address line 3
Address line 4
Post Code
QRP@QRP.example
For the business card I like the idea of front/back designs, where either there is something which joins the front and back or there is a slightly modified logo on the back... You're call, I'm open to anything here, so if you come up with something just try it out, I'll give everyone feedback where possible!
Please don't just stick my logo on a pen and say "hey, here you go...", for the pen design I'm looking for colours etc and where they are placed on the pen too!
Anything you think would look good!
Image file to show the logo
Extra images (inc psds!) for the logo

```html
<!DOCTYPE html>
<html lang="en">
<head>
<meta charset="utf-8">
<title>Morvane Advisory – Stationery</title>
<link href="https://fonts.googleapis.com/css2?family=Open+Sans:wght@400;600&display=swap" rel="stylesheet">
<style>
  :root {
    --backdrop: #e4e6e8;
    --paper: #ffffff;
    --teal: #1f8fb0;
    --teal-deep: #0f6f8e;
    --teal-soft: #cfe6ee;
    --ink: #3a3f44;
    --ink-soft: #7a8288;
    --rule: #c9d3d8;
  }
  * { box-sizing: border-box; margin: 0; padding: 0; }
  html, body { width: 1200px; height: 674px; overflow: hidden; }
  body {
    position: relative;
    background: var(--backdrop);
    font-family: "Open Sans", Arial, sans-serif;
    color: var(--ink);
  }
  .brand-name { color: var(--teal); font-weight: 600; white-space: nowrap; }
  .brand-square { background: var(--teal); border-radius: 4px; }

  /* Business card – front */
  .card { position: absolute; width: 252px; height: 130px; background: var(--paper);
          box-shadow: 0 2px 6px rgba(0,0,0,.18); overflow: hidden; }
  .card-front { left: 108px; top: 216px; }
  .card-front .details { position: absolute; left: 14px; top: 20px; width: 120px; z-index: 1;
          font-size: 6.5px; line-height: 1.5; color: var(--ink-soft); white-space: nowrap; }
  .card-front .person { font-size: 11px; color: var(--teal); font-weight: 600; }
  .card-front .role { font-size: 6.5px; margin-bottom: 5px; }
  .card-front .contact { margin-top: 4px; }
  .card-front .mark-panel { position: absolute; right: 0; top: 0; width: 118px; height: 100%;
          background: linear-gradient(90deg, var(--paper), var(--teal-soft)); }
  .card-front .mark-panel .brand-square { position: absolute; right: 30px; top: 28px; width: 66px; height: 66px; }

  /* Business card – back */
  .card-back { left: 108px; top: 396px; }
  .card-back .band { position: absolute; left: 0; top: 30px; width: 100%; height: 70px;
          background: linear-gradient(90deg, var(--teal-soft), var(--paper) 40%); }
  .card-back .brand-square { position: absolute; left: 24px; top: 28px; width: 74px; height: 74px; }
  .card-back .brand-name { position: absolute; left: 110px; top: 54px; font-size: 15px; }

  /* Letterhead */
  .letterhead { position: absolute; left: 432px; top: 36px; width: 360px; height: 600px;
          background: var(--paper); box-shadow: 0 2px 8px rgba(0,0,0,.18); }
  .letterhead .header { position: absolute; left: 24px; top: 28px; right: 20px; display: flex; justify-content: space-between; }
  .letterhead .logo { display: flex; align-items: center; gap: 8px; }
  .letterhead .logo .brand-square { width: 26px; height: 26px; }
  .letterhead .logo .brand-name { font-size: 17px; }
  .letterhead .address { border-left: 1px solid var(--rule); padding-left: 6px; font-size: 5px; line-height: 1.6; color: var(--ink-soft); width: 118px; white-space: nowrap; }
  .letterhead .address .contact { margin-top: 6px; }
  .letterhead .watermark { position: absolute; left: 84px; top: 220px; width: 170px; height: 170px;
          background: var(--teal-soft); opacity: .35; border-radius: 14px; }

  /* Envelope */
  .envelope { position: absolute; left: 684px; top: 336px; width: 396px; height: 216px;
          background: var(--paper); box-shadow: 0 2px 8px rgba(0,0,0,.2); overflow: hidden; }
  .envelope svg.flap { position: absolute; left: 0; top: 0; }
  .envelope .logo { position: absolute; left: 40px; top: 66px; display: flex; align-items: center; gap: 8px; }
  .envelope .logo .brand-square { width: 30px; height: 30px; }
  .envelope .logo .brand-name { font-size: 20px; }
  .envelope .watermark { position: absolute; right: 28px; top: 82px; width: 96px; height: 96px;
          background: var(--teal-soft); opacity: .45; border-radius: 10px; }
  .envelope .footer { position: absolute; left: 40px; bottom: 22px; font-size: 5.5px; color: var(--ink-soft); white-space: nowrap; }
</style>
</head>
<body>

  <section class="card card-front" aria-label="Business card front">
    <div class="details">
      <div class="person">Helmut Draven</div>
      <div class="role">Director</div>
      <div>Address line 1, Address line 2,</div>
      <div>Address line 3, Address line 4,</div>
      <div>Post Code</div>
      <div class="contact">T 01632 960214</div>
      <div>M 07700 900318</div>
      <div>QRP@QRP.example</div>
    </div>
    <div class="mark-panel"><div class="brand-square"></div></div>
  </section>

  <section class="card card-back" aria-label="Business card back">
    <div class="band"></div>
    <div class="brand-square"></div>
    <span class="brand-name">Morvane Advisory</span>
  </section>

  <section class="letterhead" aria-label="Letterhead">
    <div class="header">
      <div class="logo"><div class="brand-square"></div><span class="brand-name">Morvane Advisory</span></div>
      <div class="address">
        <div>Address line 1, Address line 2, Address line 3</div>
        <div>Address line 4, Post Code</div>
        <div class="contact">T 01632 960214</div>
        <div>QRP@QRP.example</div>
      </div>
    </div>
    <div class="watermark"></div>
  </section>

  <section class="envelope" aria-label="Envelope">
    <svg class="flap" width="396" height="60" viewBox="0 0 396 60">
      <defs>
        <linearGradient id="flapFill" x1="0" x2="1">
          <stop offset="0" stop-color="#0f6f8e"/>
          <stop offset="1" stop-color="#2aa3c4"/>
        </linearGradient>
      </defs>
      <path d="M0 0 H396 V22 C300 52 120 56 0 36 Z" fill="url(#flapFill)"/>
    </svg>
    <div class="logo"><div class="brand-square"></div><span class="brand-name">Morvane Advisory</span></div>
    <div class="watermark"></div>
    <div class="footer">Address line 1 | Address line 2 | Address line 3 | Address line 4 | Post Code</div>
  </section>

</body>
</html>
```